Letterhead, stationery and email signature for construction business

I need the letterhead, stationery and email signature designs for a construction business. I want them to have a corporate feel to them.

I've attached the logo for reference.

```html
<!DOCTYPE html>
<html lang="en">
<head>
<meta charset="utf-8">
<title>Kestrel Build – Stationery Set</title>
<link rel="stylesheet" href="https://fonts.googleapis.com/css2?family=Open+Sans:wght@400;600;700&family=Poppins:wght@400&display=swap">
<style>
  :root {
    --brand-blue: #2f56a2;
    --brand-blue-dark: #284a8f;
    --brand-grey: #6c7389;
    --ink: #2b2b2b;
    --faint: #eff0f7;
    --paper: #ffffff;
    --scene-grey: #b8b7b9;
    --shadow: 0 4px 8px rgba(0,0,0,.28);
  }
  * { box-sizing: border-box; margin: 0; padding: 0; }
  html, body { width: 756px; height: 1200px; overflow: hidden; background: var(--paper); }
  body { font-family: "Open Sans", sans-serif; color: var(--ink); }
  .canvas { position: relative; width: 756px; height: 1200px; overflow: hidden; background: var(--paper); }
  .sheet { position: absolute; background: var(--paper); box-shadow: var(--shadow); overflow: hidden; }

  /* brand name lockup */
  .brand { position: absolute; display: flex; align-items: center; gap: 4px; white-space: nowrap; }
  .brand-square { background: var(--brand-blue); flex: none; }
  .brand-name { font-family: "Open Sans", sans-serif; font-weight: 700; color: var(--brand-blue); letter-spacing: .02em; line-height: 1; }
  .brand--white .brand-square { background: #fff; }
  .brand--white .brand-name { color: #fff; }

  .contact-list { position: absolute; list-style: none; line-height: 1.3; }
  .contact-list li { display: flex; align-items: center; gap: 3px; }
  .icon { width: 1em; height: 1em; fill: var(--brand-blue); flex: none; }

  .faint-block { position: absolute; background: var(--faint); }

  /* letterhead */
  .letterhead { left: 85px; top: 61px; width: 270px; height: 381px; }
  .letterhead .brand { left: 14px; top: 20px; }
  .letterhead .brand-square { width: 24px; height: 24px; }
  .letterhead .brand-name { font-size: 15px; }
  .letterhead .divider { position: absolute; left: 177px; top: 15px; width: 1px; height: 39px; background: var(--brand-blue); }
  .letterhead .contact-list { left: 187px; top: 14px; font-size: 5.8px; }
  .letterhead .faint-block { left: 38px; top: 70px; width: 195px; height: 230px; }
  .letterhead .footer-band { position: absolute; left: 0; bottom: 0; width: 270px; height: 18px; }

  /* email signature */
  .signature { left: 388px; top: 41px; width: 315px; height: 112px; }
  .signature .brand { left: 48px; top: 23px; }
  .signature .brand-square { width: 22px; height: 22px; }
  .signature .brand-name { font-size: 13.5px; }
  .signature .follow { position: absolute; left: 40px; top: 75px; width: 130px; text-align: center; font-family: "Poppins", sans-serif; font-size: 7.5px; color: #333; }
  .signature .social { position: absolute; left: 82px; top: 87px; display: flex; gap: 4px; }
  .signature .social span { width: 8px; height: 8px; border-radius: 50%; background: var(--brand-blue); }
  .signature .divider { position: absolute; left: 172px; top: 18px; width: 1px; height: 77px; background: var(--brand-blue); }
  .signature .person-name { position: absolute; left: 183px; top: 15px; font-size: 10px; font-weight: 700; color: var(--brand-blue); }
  .signature .person-role { position: absolute; left: 183px; top: 28px; font-size: 7px; }
  .signature .address { position: absolute; left: 183px; top: 40px; font-size: 7px; line-height: 1.35; }
  .signature .contact-list { left: 183px; top: 67px; font-size: 7px; line-height: 1.35; }

  /* envelope back */
  .envelope-back { left: 388px; top: 169px; width: 276px; height: 121px; }
  .envelope-back .flap { position: absolute; left: 0; top: 0; width: 276px; height: 36px; background: var(--paper); border-radius: 0 0 16px 16px; box-shadow: 0 3px 5px rgba(0,0,0,.18); }
  .envelope-back .brand { left: 50%; top: 8px; transform: translateX(-50%); }
  .envelope-back .brand-square { width: 12px; height: 12px; }
  .envelope-back .brand-name { font-size: 7px; }

  /* envelope front */
  .envelope-front { left: 388px; top: 323px; width: 276px; height: 120px; }
  .envelope-front .brand { left: 8px; top: 12px; }
  .envelope-front .brand-square { width: 20px; height: 20px; }
  .envelope-front .brand-name { font-size: 12px; }
  .envelope-front .return-address { position: absolute; left: 8px; top: 97px; font-size: 5.5px; line-height: 1.35; }
  .envelope-front .faint-block { left: 177px; top: 7px; width: 99px; height: 110px; }

  /* presentation folder */
  .folder-stage { position: absolute; left: 105px; top: 478px; width: 540px; height: 660px; background: var(--scene-grey); }
  .folder-panel { position: absolute; width: 230px; height: 300px; overflow: hidden; box-shadow: 0 4px 10px rgba(0,0,0,.25); }
  .folder-back { left: 40px; top: 14px; background: var(--brand-blue); }
  .folder-back .brand { left: 22px; top: 96px; }
  .folder-back .brand-square { width: 30px; height: 30px; }
  .folder-back .brand-name { font-size: 17px; }
  .folder-back .contact-block { position: absolute; left: 22px; bottom: 26px; color: #fff; font-size: 6.5px; }
  .folder-back .contact-block .address { padding-bottom: 5px; margin-bottom: 5px; border-bottom: 1px solid rgba(255,255,255,.7); width: 110px; }
  .folder-back .contact-block ul { list-style: none; display: flex; gap: 6px; }
  .folder-back .contact-block li { display: flex; align-items: center; gap: 2px; }
  .folder-back .icon { fill: #fff; }
  .folder-front { left: 270px; top: 14px; background: var(--paper); }
  .folder-front .cover-mark { position: absolute; left: 30px; top: 40px; width: 170px; height: 190px; background: linear-gradient(135deg, var(--brand-grey) 0%, var(--brand-blue) 65%, var(--brand-blue-dark) 100%); }
  .folder-front .cover-stripes { position: absolute; left: 0; bottom: 18px; width: 230px; }
  .folder-front .cover-stripes span { display: block; height: 3px; background: #4a4d5c; margin-bottom: 2px; }
  .folder-front .cover-stripes span + span { background: var(--brand-blue); }

  .folder-inside-left { left: 40px; top: 342px; background: linear-gradient(90deg, #fff 0%, #f4f4f4 55%, #c9c9c9 100%); }
  .folder-inside-left .pocket { position: absolute; left: 0; bottom: 0; width: 230px; height: 110px; }
  .folder-inside-right { left: 270px; top: 342px; background: linear-gradient(90deg, #d6d6d6 0%, #f4f4f4 20%, #fff 60%); }
  .folder-inside-right .pocket { position: absolute; left: 0; bottom: 0; width: 230px; height: 130px; }

  .insert-letter { position: absolute; left: 22px; top: 14px; width: 186px; height: 240px; background: var(--paper); box-shadow: 0 1px 4px rgba(0,0,0,.2); }
  .insert-letter .brand { left: 9px; top: 14px; }
  .insert-letter .brand-square { width: 14px; height: 14px; }
  .insert-letter .brand-name { font-size: 8.5px; }
  .insert-letter .divider { position: absolute; left: 118px; top: 10px; width: 1px; height: 24px; background: var(--brand-blue); }
  .insert-letter .contact-list { left: 123px; top: 9px; font-size: 3.8px; }
  .insert-letter .rule { position: absolute; left: 9px; right: 9px; top: 40px; height: 1px; background: var(--brand-blue); }
  .insert-letter .faint-block { left: 50px; top: 55px; width: 110px; height: 120px; }
  .letter-body { position: absolute; left: 10px; top: 52px; width: 166px; font-size: 4px; line-height: 1.45; }
  .letter-body p { margin-bottom: 3px; }
  .letter-body .salutation { font-weight: 700; font-size: 5px; }
</style>
</head>
<body>
<svg width="0" height="0" style="position:absolute" aria-hidden="true">
  <symbol id="i-phone" viewBox="0 0 10 10"><path d="M2 1h2l1 2-1.2 1a6 6 0 0 0 2.2 2.2L7 5l2 1v2c0 .6-.4 1-1 1A8 8 0 0 1 1 2c0-.6.4-1 1-1z"/></symbol>
  <symbol id="i-mail" viewBox="0 0 10 10"><path d="M1 2.5h8v5H1z M1 2.5l4 3 4-3" stroke="#fff" stroke-width=".6"/></symbol>
  <symbol id="i-globe" viewBox="0 0 10 10"><circle cx="5" cy="5" r="4"/><path d="M1 5h8M5 1c-2 2.5-2 5.5 0 8M5 1c2 2.5 2 5.5 0 8" stroke="#fff" stroke-width=".6" fill="none"/></symbol>
</svg>

<main class="canvas">

  <section class="sheet letterhead" aria-label="Letterhead">
    <div class="brand"><span class="brand-square"></span><span class="brand-name">KESTREL BUILD</span></div>
    <span class="divider"></span>
    <ul class="contact-list">
      <li>Your address, City</li>
      <li>State, Zip 1234</li>
      <li><svg class="icon"><use href="#i-phone"/></svg>123 456 789</li>
      <li><svg class="icon"><use href="#i-mail"/></svg>info@kestrelbuild.example</li>
      <li><svg class="icon"><use href="#i-globe"/></svg>www.kestrelbuild.example</li>
    </ul>
    <div class="faint-block"></div>
    <svg class="footer-band" viewBox="0 0 270 18" aria-hidden="true">
      <polygon points="0,2 170,2 166,6 0,6" fill="var(--brand-grey)"/>
      <polygon points="0,8 168,8 176,0 270,0 270,18 0,18" fill="var(--brand-blue)"/>
    </svg>
  </section>

  <section class="sheet signature" aria-label="Email signature">
    <div class="brand"><span class="brand-square"></span><span class="brand-name">KESTREL BUILD</span></div>
    <p class="follow">Click below to follow us</p>
    <div class="social"><span></span><span></span><span></span><span></span></div>
    <span class="divider"></span>
    <p class="person-name">OWEN MARSH</p>
    <p class="person-role">Managing Director</p>
    <p class="address">Your address, City<br>State, Zip 1234</p>
    <ul class="contact-list">
      <li><svg class="icon"><use href="#i-phone"/></svg>123-456-789</li>
      <li><svg class="icon"><use href="#i-mail"/></svg>contact@kestrelbuild.example</li>
      <li><svg class="icon"><use href="#i-globe"/></svg>www.kestrelbuild.example</li>
    </ul>
  </section>

  <section class="sheet envelope-back" aria-label="Envelope back">
    <div class="flap">
      <div class="brand"><span class="brand-square"></span><span class="brand-name">KESTREL BUILD</span></div>
    </div>
  </section>

  <section class="sheet envelope-front" aria-label="Envelope front">
    <div class="brand"><span class="brand-square"></span><span class="brand-name">KESTREL BUILD</span></div>
    <p class="return-address">Your address, City<br>State, Zip 1234</p>
    <div class="faint-block"></div>
  </section>

  <section class="folder-stage" aria-label="Presentation folder">
    <div class="folder-panel folder-back">
      <div class="brand brand--white"><span class="brand-square"></span><span class="brand-name">KESTREL BUILD</span></div>
      <div class="contact-block">
        <p class="address">Your address, City State, Zip 1234</p>
        <ul>
          <li><svg class="icon"><use href="#i-phone"/></svg>123 456 789</li>
          <li><svg class="icon"><use href="#i-mail"/></svg>info@kestrelbuild.example</li>
        </ul>
        <ul style="margin-top:3px">
          <li><svg class="icon"><use href="#i-globe"/></svg>www.kestrelbuild.example</li>
        </ul>
      </div>
    </div>

    <div class="folder-panel folder-front">
      <div class="cover-mark" role="img" aria-label="Large brand emblem area in blue and slate"></div>
      <div class="cover-stripes"><span></span><span></span></div>
    </div>

    <div class="folder-panel folder-inside-left">
      <svg class="pocket" viewBox="0 0 230 110" preserveAspectRatio="none" aria-hidden="true">
        <path d="M0,30 L150,8 Q168,5 176,18 L230,110 L0,110 Z" fill="var(--brand-blue)"/>
      </svg>
    </div>

    <div class="folder-panel folder-inside-right">
      <article class="insert-letter">
        <div class="brand"><span class="brand-square"></span><span class="brand-name">KESTREL BUILD</span></div>
        <span class="divider"></span>
        <ul class="contact-list">
          <li>Your address, City</li>
          <li>State, Zip 1234</li>
          <li><svg class="icon"><use href="#i-phone"/></svg>123 456 789</li>
          <li><svg class="icon"><use href="#i-mail"/></svg>info@kestrelbuild.example</li>
          <li><svg class="icon"><use href="#i-globe"/></svg>www.kestrelbuild.example</li>
        </ul>
        <span class="rule"></span>
        <div class="faint-block"></div>
        <div class="letter-body">
          <p>January-03-2020</p>
          <p>Mr. Alan Reed<br>President</p>
          <p>Northfield Corporation<br>45 Market Street, Suite 10<br>City, State, 120023</p>
          <p class="salutation">Dear Mr. Reed,</p>
          <p>Thank you for meeting with our team last week. We are pleased to share the project outline and schedule.</p>
          <p>Our crew will begin site work in early spring and report progress every month.</p>
        </div>
      </article>
      <svg class="pocket" viewBox="0 0 230 130" preserveAspectRatio="none" aria-hidden="true">
        <path d="M0,40 L205,0 L230,60 L230,130 L0,130 Z" fill="var(--brand-grey)"/>
      </svg>
    </div>
  </section>

</main>
</body>
</html>
```